Our swimming pool service needs your help with letterhead

Letterhead for small swimming pool service- We would like a professional look with a creative layout- must be compatible with QuickBooks forms (sample attached)
No more than 2 colors in graphics

Target Market(s)

Homeowners/ Contractors

Font styles to use
Sans Serif

Colors
33a6d7
85cae6

Requirements
Must have
• Logo (file attached)
• Compatible with QuickBooks (sample attached)
• Mailing address- P.O. Box 52, Harlow Bend NY 11603
• phone- (631) 582-9016
• email- marcotrentpools@fernmail.test
• Licensed & Insured
Nice to have
• Small slogan- Examples:Family owned and operated for 25 years, 25 years of trusted service
• Creative layout
Should not have
• Blue color must be same as blue in our logo
• No thick lines of color
• No design in middle of page

```html
<!DOCTYPE html>
<html lang="en">
<head>
<meta charset="utf-8">
<title>Marco Trent Pool Service – Letterhead</title>
<link rel="stylesheet" href="https://fonts.googleapis.com/css2?family=Roboto+Condensed:wght@400;500&family=Arimo:ital,wght@0,400;1,700&display=swap">
<style>
  :root {
    --navy: #233a5e;
    --sky: #6cb0e0;
    --ink: #1b1b1b;
    --paper: #ffffff;
  }
  html, body {
    margin: 0;
    padding: 0;
    overflow: hidden;
    background: var(--paper);
  }
  .letterhead {
    position: relative;
    width: 849px;
    height: 1200px;
    overflow: hidden;
    background: var(--paper);
    font-family: "Roboto Condensed", Arial, sans-serif;
  }
  .brand {
    position: absolute;
    left: 26px;
    top: 46px;
    display: flex;
    align-items: center;
    gap: 12px;
  }
  .brand-dot {
    width: 40px;
    height: 40px;
    border-radius: 50%;
    background: var(--sky);
    flex: none;
  }
  .brand-name {
    font-family: "Roboto Condensed", Arial, sans-serif;
    font-weight: 500;
    font-size: 29px;
    line-height: 1;
    letter-spacing: 1px;
    color: var(--navy);
    text-transform: uppercase;
    margin: 0;
  }
  .brand-tag {
    position: absolute;
    left: 80px;
    top: 94px;
    margin: 0;
    font-size: 17px;
    color: var(--navy);
    letter-spacing: 0.5px;
  }
  .contact {
    position: absolute;
    left: 533px;
    top: 44px;
    width: 316px;
    height: 76px;
    border-bottom: 2px solid var(--sky);
  }
  .contact-divider {
    position: absolute;
    left: 21px;
    top: 4px;
    height: 60px;
    border-left: 1px dotted var(--sky);
  }
  .contact-list {
    list-style: none;
    margin: 0;
    padding: 0;
  }
  .contact-item {
    position: absolute;
    left: 0;
    display: flex;
    align-items: center;
    font-size: 13px;
    color: var(--ink);
    white-space: nowrap;
  }
  .contact-item svg {
    width: 14px;
    height: 12px;
    margin-left: 3px;
    margin-right: 23px;
  }
  .contact-item:nth-child(1) { top: 2px; }
  .contact-item:nth-child(2) { top: 22px; }
  .contact-item:nth-child(3) { top: 42px; }
  .footer-rule {
    position: absolute;
    left: 0;
    top: 1136px;
  }
  .slogan-number {
    position: absolute;
    left: 423px;
    top: 1130px;
    margin: 0;
    font-family: "Arimo", Arial, sans-serif;
    font-style: italic;
    font-weight: 700;
    font-size: 44px;
    letter-spacing: -4px;
    color: var(--sky);
    line-height: 1;
  }
  .slogan-text {
    position: absolute;
    left: 461px;
    top: 1157px;
    margin: 0;
    font-family: "Arimo", Arial, sans-serif;
    font-size: 10.5px;
    line-height: 11px;
    color: var(--navy);
  }
  .slogan-text span { display: block; }
  .slogan-text span:first-child { padding-left: 8px; }
</style>
</head>
<body>
<main class="letterhead">
  <header>
    <div class="brand">
      <span class="brand-dot" aria-hidden="true"></span>
      <h1 class="brand-name">Marco Trent Pool Service</h1>
    </div>
    <p class="brand-tag">Licensed &amp; Insured</p>

    <address class="contact">
      <span class="contact-divider" aria-hidden="true"></span>
      <ul class="contact-list">
        <li class="contact-item">
          <svg viewBox="0 0 14 12" aria-hidden="true" fill="none" stroke="#6cb0e0" stroke-width="0.9">
            <rect x="1" y="4" width="12" height="6.5" rx="1"/>
            <path d="M7 4v-3h3"/>
          </svg>
          Mailing Address: P.O. Box 52, Harlow Bend NY 11603
        </li>
        <li class="contact-item">
          <svg viewBox="0 0 14 12" aria-hidden="true" fill="none" stroke="#6cb0e0" stroke-width="0.9">
            <circle cx="7" cy="6" r="5.3"/>
            <path d="M5.5 3.3c-1 1.5-.5 4 1.5 5.5l1-1"/>
          </svg>
          Phone- (631) 582-9016
        </li>
        <li class="contact-item">
          <svg viewBox="0 0 14 12" aria-hidden="true" fill="none" stroke="#6cb0e0" stroke-width="0.9">
            <rect x="1.5" y="2.5" width="11" height="7.5"/>
            <path d="M1.5 2.5l5.5 4.5 5.5-4.5M1.5 10l4-3.5M12.5 10l-4-3.5"/>
          </svg>
          E-mail marcotrentpools@fernmail.test
        </li>
      </ul>
    </address>
  </header>

  <footer>
    <svg class="footer-rule" width="849" height="64" viewBox="0 0 849 64" aria-hidden="true">
      <path d="M0 56H444L480 1H849" fill="none" stroke="#6cb0e0" stroke-width="2"/>
    </svg>
    <p class="slogan-number">25</p>
    <p class="slogan-text"><span>Years of</span><span>Trusted Service</span></p>
  </footer>
</main>
</body>
</html>
```